Artistic Poster for a Short Film

I am the Writer/Director of an upcoming short film called "Driftwater" and I need a 20x30 poster for the project screening. The screening is coming up very soon so apologies for the quick turnaround time. Here is a short synopsis:

"Owen is a mysterious man who is lost and disoriented. With the help of Marisol, he searches for items out of an old diary written long ago by a woman named Greta, despite not understanding exactly why he does so. Marisol helps, but when they are unsuccessful she confronts Owen: Does he know why he restlessly searches for these items? The truth is shocking, and reveals Owen's connections to Marisol, Greta, and the strange old diary.

The truth is that Owen is actually an old man, and Marisol is his caretaker and granddaughter. His memories, including those of Greta, his deceased wife, have been destroyed by Dementia. He often wakes believing himself to be at an earlier stage of his life, and therefore meets many of the challenges of life with anger and confusion."

Here is the film's website: http://www.driftwater-film.example
Here is our successful Fundhive: http://www.fundhive.example/projects/482617305/driftwater-a-short-film

The design should be dark and simple. I'm a fan of the art-prints that this short film used (scroll down to see): http://www.fundhive.example/projects/marcuvolden/ember-a-short-film-based-on-the-story-by-lydia-crane but I'm also open to other ideas. If you google "alternative movie posters" you'll see what I mean. The poster should be simple, easy to read, and hint at the themes of the film without giving the twist away.

Here is a link to the Fine Cut of the film: https://clipvault.example/51204977 The password is: lanterns47
It is not a completed version but will give you an idea of what the film will look like.

Target Market(s)

The intended audience is an art-film crowd of moviegoers.

Industry/Entity Type

Movie

Requirements
Must have
• The poster must have the typical movie poster text at the bottom. The information that should be included is: First line: HOLLOW BIRCH PRODUCTIONS presents a film by DANIEL OKAFOR "DRIFTWATER" MATTHIEU LAVERNE TORI BALSDEN
Second line: music by OLAF BRISK director of photography CALVIN R. OSTROM edited by ELIAS VOSS costume designer JOSELYNE TARRAW
Third line: produced by IVY KOWALCZE DANIEL OKAFOR written and directed by DANIEL OKAFOR

It should have the title of the film "Driftwater" and "A film by Daniel Okafor" on the poster (in addition to the text at the bottom.

It must be high-quality and printable to a size of 20x30. Ideal resolution is 6060x9090. I only need the high quality printable file, I will do the printing myself.
Should not have
• Bright colors.

```html
<!DOCTYPE html>
<html lang="en">
<head>
<meta charset="utf-8">
<title>Driftwater — a film by Daniel Okafor</title>
<link href="https://fonts.googleapis.com/css2?family=Cinzel:wght@400;500&family=Felipa&family=Oswald:wght@400&display=swap" rel="stylesheet">
<style>
  :root {
    --ink-deep: #120d0a;
    --ink-warm: #3a2516;
    --haze: #6f6a62;
    --rust: #9e4b22;
    --rust-script: #914420;
    --credit: #ece4dc;
  }
  html, body {
    margin: 0;
    padding: 0;
    width: 800px;
    height: 1200px;
    overflow: hidden;
    background: var(--ink-deep);
  }
  .poster {
    position: relative;
    width: 800px;
    height: 1200px;
    overflow: hidden;
    background: var(--ink-deep);
  }
  .poster__scene {
    position: absolute;
    inset: 0;
    background:
      radial-gradient(ellipse 120px 90px at 470px 170px, rgba(238,214,170,0.55), transparent 70%),
      radial-gradient(ellipse 220px 260px at 640px 420px, rgba(150,150,145,0.55), transparent 75%),
      radial-gradient(ellipse 260px 320px at 300px 460px, rgba(110,70,35,0.55), transparent 75%),
      linear-gradient(180deg, #2a1d14 0%, #3b2a1d 30%, #2a1f18 55%, #120d0a 62%, #0d0907 100%);
  }
  .poster__type {
    position: absolute;
    inset: 0;
  }
  .title-line {
    font-family: "Cinzel", serif;
    font-size: 98px;
    fill: var(--rust);
  }
  .title-line .initial { font-size: 104px; }
  .byline {
    font-family: "Felipa", cursive;
    font-size: 46px;
    fill: var(--rust-script);
  }
  .credits {
    font-family: "Oswald", sans-serif;
    font-size: 13px;
    fill: var(--credit);
    letter-spacing: 1px;
  }
</style>
</head>
<body>
<main class="poster">
  <div class="poster__scene" role="img" aria-label="Dim warm interior with a caged hanging bulb and silhouetted figures against a bright doorway"></div>
  <svg class="poster__type" width="800" height="1200" viewBox="0 0 800 1200">
    <g class="title-stack">
      <text class="title-line" x="133" y="112" textLength="582" lengthAdjust="spacingAndGlyphs"><tspan class="initial">D</tspan>riftwater</text>
      <text class="title-line" x="133" y="210" textLength="582" lengthAdjust="spacingAndGlyphs"><tspan class="initial">D</tspan>riftwater</text>
      <text class="title-line" x="133" y="307" textLength="582" lengthAdjust="spacingAndGlyphs"><tspan class="initial">D</tspan>riftwater</text>
      <text class="title-line" x="133" y="404" textLength="582" lengthAdjust="spacingAndGlyphs"><tspan class="initial">D</tspan>riftwater</text>
      <text class="title-line" x="133" y="501" textLength="582" lengthAdjust="spacingAndGlyphs"><tspan class="initial">D</tspan>riftwater</text>
      <text class="title-line" x="133" y="599" textLength="582" lengthAdjust="spacingAndGlyphs"><tspan class="initial">D</tspan>riftwater</text>
      <text class="title-line" x="133" y="696" textLength="582" lengthAdjust="spacingAndGlyphs"><tspan class="initial">D</tspan>riftwater</text>
      <text class="title-line" x="133" y="793" textLength="582" lengthAdjust="spacingAndGlyphs"><tspan class="initial">D</tspan>riftwater</text>
      <text class="title-line" x="133" y="890" textLength="582" lengthAdjust="spacingAndGlyphs"><tspan class="initial">D</tspan>riftwater</text>
    </g>
    <text class="byline" x="108" y="988" textLength="608" lengthAdjust="spacingAndGlyphs">a film by Daniel Okafor</text>
    <g class="credits">
      <text x="40" y="1081" textLength="720" lengthAdjust="spacingAndGlyphs">HOLLOW BIRCH PRODUCTIONS PRESENTS A FILM BY DANIEL OKAFOR "DRIFTWATER" MATTHIEU LAVERNE TORI</text>
      <text x="40" y="1106" textLength="720" lengthAdjust="spacingAndGlyphs">BALSDEN MUSIC BY OLAF BRISK DIRECTOR OF PHOTOGRAPHY CALVIN R. OSTROM EDITED BY ELIAS VOSS COSTUME</text>
      <text x="103" y="1131" textLength="594" lengthAdjust="spacingAndGlyphs">DESIGNER JOSELYNE TARRAW PRODUCED BY IVY KOWALCZE DANIEL OKAFOR WRITTEN AND</text>
      <text x="400" y="1156" text-anchor="middle">DIRECTED BY DANIEL OKAFOR</text>
    </g>
  </svg>
</main>
</body>
</html>
```